- Redesign our business card
- Logo remains unchanged
- Current business card attached

Target Market(s)

We are a property management company

Industry/Entity Type

Business

```html
<!DOCTYPE html>
<html lang="en">
<head>
<meta charset="utf-8">
<title>Hartwell Property Group – Business Card</title>
<link rel="stylesheet" href="https://fonts.googleapis.com/css2?family=Arimo:wght@400;700&family=Roboto+Condensed:wght@700&display=swap">
<style>
  :root {
    --olive: #6d7a3e;
    --slate: #625f5e;
    --sand: #d3c89d;
    --ink: #231f20;
    --paper: #ffffff;
    --bg-light: #4b6b1e;
    --bg-dark: #1e1b19;
  }
  * { margin: 0; padding: 0; box-sizing: border-box; }
  html, body { width: 1200px; height: 1200px; overflow: hidden; }
  body {
    position: relative;
    background: linear-gradient(135deg, var(--bg-light) 0%, #2c3318 38%, var(--bg-dark) 62%, var(--bg-dark) 100%);
    font-family: "Arimo", Arial, sans-serif;
    color: var(--ink);
  }
  .card {
    position: absolute;
    width: 795px;
    height: 440px;
    border-radius: 30px;
    overflow: hidden;
  }
  .card-front { left: 72px; top: 142px; background: var(--paper); }
  .card-back { left: 333px; top: 615px; background: var(--sand); }

  .brand { position: absolute; left: 355px; top: 86px; }
  .brand-mark { width: 62px; height: 62px; background: var(--olive); margin-bottom: 22px; }
  .brand-name {
    font-size: 17px; font-weight: 700; color: var(--olive);
    letter-spacing: 0.2px; white-space: nowrap;
  }
  .brand-tagline {
    font-size: 11.5px; color: #6a6664; letter-spacing: 0.3px;
    margin-top: 3px; white-space: nowrap;
  }

  .person { position: absolute; left: 52px; top: 212px; }
  .person-name {
    font-family: "Roboto Condensed", "Arial Narrow", sans-serif;
    font-size: 24px; font-weight: 700; color: var(--ink);
  }
  .person-title { font-size: 16px; margin-top: 6px; color: #3a3636; }

  .address { position: absolute; left: 355px; top: 246px; font-size: 18px; line-height: 26px; color: var(--ink); }

  .contacts { position: absolute; left: 355px; top: 312px; list-style: none; font-size: 18px; }
  .contacts li { display: flex; align-items: center; height: 25.5px; }
  .contacts .label {
    width: 14px; height: 14px; background: var(--olive); color: var(--paper);
    font-size: 10px; font-weight: 700; line-height: 14px; text-align: center;
    margin-right: 23px;
  }

  .back-name {
    position: absolute; left: 30px; top: 78px;
    font-size: 26px; font-weight: 700; color: var(--olive); white-space: nowrap;
  }
  .back-block { position: absolute; left: 127px; top: 170px; width: 270px; height: 270px; background: var(--slate); }

  .services { position: absolute; left: 455px; top: 228px; list-style: none; }
  .services li {
    display: flex; align-items: center; height: 39px;
    font-family: "Roboto Condensed", "Arial Narrow", sans-serif;
    font-size: 21px; font-weight: 700; color: var(--ink);
  }
  .services li::before {
    content: ""; width: 11px; height: 14px; background: var(--paper); margin-right: 12px;
  }
  .website {
    position: absolute; left: 479px; top: 386px;
    font-family: "Roboto Condensed", "Arial Narrow", sans-serif;
    font-size: 20px; font-weight: 700; color: var(--olive);
  }
</style>
</head>
<body>
  <section class="card card-front">
    <div class="brand">
      <div class="brand-mark"></div>
      <div class="brand-name">HARTWELL PROPERTY GROUP</div>
      <div class="brand-tagline">STRATA MANAGEMENT SERVICES</div>
    </div>
    <div class="person">
      <div class="person-name">Daniel Hartley</div>
      <div class="person-title">Licensed Strata Manager</div>
    </div>
    <address class="address" style="font-style:normal">
      PO Box 48, Greenfield NSW 2150<br>
      12/5-19 Lindon Street Parkvale NSW 2041
    </address>
    <ul class="contacts">
      <li><span class="label">T</span>02 9000 1470</li>
      <li><span class="label">F</span>02 9000 1485</li>
      <li><span class="label">M</span>0400 372 918</li>
      <li><span class="label">E</span>info@hartwellproperty.com.au</li>
    </ul>
  </section>

  <section class="card card-back">
    <div class="back-name">HARTWELL PROPERTY GROUP</div>
    <div class="back-block"></div>
    <ul class="services">
      <li>Strata Management</li>
      <li>Community Management</li>
      <li>Property Management</li>
    </ul>
    <div class="website">www.hartwellproperty.com.au</div>
  </section>
</body>
</html>
```